Advert for e-news letter

I have a property valuation business and this is an advert for one specific service. The service is for Lot Entitlements and is directed at conveyancers. I have attached a company logo. The sizing of the advert (as noted in Media kit) – will be 158px x 170 px.
Advert to summarise the following;
Do you have developer clients? We can help with Lot Entitlements for Land Division. We believe that our prices are the best in the market, however should you provide a cheaper written quote we will beat it by 15%.
Pricing for RVB compliant Lot Entitlement Certificates.
• 1 Allotment into 2 Community Titled Lots: $220 Inc GST (2 day turnaround)
• 1 Allotment into 3 Community Titled Lots: $275 Inc GST (2 day turnaround)
• 1 Allotment into 4 or 5 Community Titled Lots: $330 Inc GST (2 day turnaround)
• 6 or more or Commercial: By Quote

```html
<!DOCTYPE html>
<html lang="en">
<head>
<meta charset="utf-8">
<title>Lot Entitlements Advert</title>
<link href="https://fonts.googleapis.com/css2?family=Arimo:wght@400;700&family=Nunito+Sans:wght@700&display=swap" rel="stylesheet">
<style>
  :root {
    --frame-blue: #1aa3e4;
    --red-top: #e8173f;
    --red-mid: #ed6b6d;
    --red-bottom: #c21d3a;
    --ink: #222222;
    --logo-ink: #333333;
    --logo-teal: #1fa89e;
    --white: #ffffff;
  }
  html, body {
    margin: 0;
    padding: 0;
    width: 1188px;
    height: 1200px;
    overflow: hidden;
    background: var(--white);
  }
  .canvas {
    position: relative;
    width: 1188px;
    height: 1200px;
  }
  .advert {
    position: absolute;
    left: 221px;
    top: 203px;
    width: 655px;
    height: 705px;
    border: 4px solid var(--frame-blue);
    background: var(--white);
    overflow: hidden;
  }
  .red-panel {
    position: absolute;
    left: 0;
    top: 146px;
    width: 100%;
    height: 559px;
    background: linear-gradient(180deg, var(--red-top) 0%, var(--red-mid) 50%, var(--red-bottom) 100%);
  }
  .banner {
    position: absolute;
    left: 0;
    top: 0;
    width: 655px;
    height: 705px;
  }
  .banner-text {
    font-family: "Arimo", Arial, sans-serif;
    font-weight: 700;
    font-size: 37px;
    fill: var(--ink);
  }
  .brand {
    position: absolute;
    left: 382px;
    top: 32px;
    display: flex;
    align-items: center;
    gap: 22px;
  }
  .brand-mark {
    width: 56px;
    height: 56px;
    background: var(--logo-teal);
  }
  .brand-name {
    font-family: "Arimo", Arial, sans-serif;
    font-weight: 700;
    font-size: 50px;
    letter-spacing: 1px;
    color: var(--logo-ink);
  }
  .pitch {
    position: absolute;
    left: 32px;
    top: 222px;
    margin: 0;
    font-family: "Nunito Sans", sans-serif;
    font-weight: 700;
    font-size: 31px;
    line-height: 40px;
    color: var(--white);
  }
  .pitch .big {
    font-size: 46px;
  }
  .pricing {
    position: absolute;
    left: 397px;
    top: 175px;
    width: 250px;
    font-family: "Arimo", Arial, sans-serif;
    color: var(--white);
  }
  .pricing-title {
    margin: 0 0 6px;
    font-size: 19.5px;
    font-weight: 700;
    line-height: 25px;
  }
  .price-list {
    list-style: none;
    margin: 0;
    padding: 0;
    font-size: 19.5px;
    line-height: 28.5px;
  }
  .price-list li {
    position: relative;
    padding-left: 12px;
    margin-bottom: 0;
  }
  .price-list li::before {
    content: "•";
    position: absolute;
    left: -2px;
    font-size: 15px;
  }
  .turnaround {
    display: block;
    line-height: 22px;
    margin-top: -3px;
    margin-bottom: 4px;
  }
</style>
</head>
<body>
<div class="canvas">
  <div class="advert">
    <div class="red-panel"></div>

    <svg class="banner" viewBox="0 0 655 705" aria-hidden="true">
      <defs>
        <linearGradient id="bannerFill" x1="0" y1="0" x2="1" y2="0.4">
          <stop offset="0" stop-color="#ffe600"/>
          <stop offset="0.45" stop-color="#fff8c8"/>
          <stop offset="0.75" stop-color="#fff2a0"/>
          <stop offset="1" stop-color="#ffe000"/>
        </linearGradient>
        <linearGradient id="bannerShadow" x1="0" y1="0" x2="0" y2="1">
          <stop offset="0" stop-color="#7a0a1c" stop-opacity="0.6"/>
          <stop offset="1" stop-color="#7a0a1c" stop-opacity="0"/>
        </linearGradient>
        <path id="lineTop" d="M72 50 C150 60 220 100 300 150"/>
        <path id="lineBottom" d="M10 124 C120 130 220 180 340 258"/>
      </defs>
      <path d="M0 170 C130 160 230 215 360 290 L350 300 C230 225 130 180 0 190 Z" fill="url(#bannerShadow)"/>
      <path d="M0 40 C60 20 130 22 200 60 C260 92 320 122 373 124 C368 190 360 240 355 283 C250 262 170 180 0 170 Z" fill="url(#bannerFill)"/>
      <text class="banner-text"><textPath href="#lineTop">Do you have</textPath></text>
      <text class="banner-text"><textPath href="#lineBottom">developer clients?</textPath></text>
    </svg>

    <div class="brand">
      <span class="brand-mark"></span>
      <span class="brand-name">NVQ</span>
    </div>

    <p class="pitch">
      We can<br>
      help with<br>
      Lot Entitlements for<br>
      Land Division. We<br>
      believe that our<br>
      prices are the best in<br>
      the market, however<br>
      should you provide a<br>
      cheaper written<br>
      quote we will beat it<br>
      by <span class="big">15%.</span>
    </p>

    <div class="pricing">
      <h2 class="pricing-title">Pricing for RVB<br>compliant Lot<br>Entitlement<br>Certificates.</h2>
      <ul class="price-list">
        <li>1 Allotment into 2<br>Community Titled<br>Lots: $220 Inc GST<span class="turnaround">(2 day turnaround)</span></li>
        <li>1 Allotment into 3<br>Community Titled<br>Lots: $275 Inc GST<span class="turnaround">(2 day turnaround)</span></li>
        <li>1 Allotment into 4 or 5<br>Community Titled<br>Lots: $330 Inc GST<span class="turnaround">(2 day turnaround)</span></li>
        <li>6 or more or<br>Commercial: By Quote</li>
      </ul>
    </div>
  </div>
</div>
</body>
</html>
```